www.DeliaBrunwick.com

I am looking to redesign my author website. I want it to reflect my personality but look more professional AND more marketing savvy.

I am looking for:
- a header/banner with JUST MY NAME:
Delia Brunwick

- a header/banner using my name and log line - like this:
Delia Brunwick
Professional Writer. Amateur Mom.

- And a logo using my name and a different log line:
Delia Brunwick
Finding the funny in parenthood before somebody loses an eye.

- social media buttons for Drovely, Quenlo, Brimsetta, vostraloom, Tarvio +.

Regarding the design style I want to use the attached design for the basis of the website. I would like to use the logo in the UPPER RIGHT HAND CORNER of the four designs attached. It is the design with the slate blue background and yellowish/orangish colors.

I LOVE the typewriter font and would like to use that for my column headers - ideally, I would love it if when you roll over the headers it looks like they are being typed out - but I don't know if that is possible. If it isn't, happy just just get the headers in that font.

Target Market(s)

30-50 year old parents and educators. My target audience is educated with a great sense of style and sense of humor.

Industry/Entity Type

Marketing

Requirements
Must have
• - Clear, bold, client friendly design/buttons
- Professional, web-savvy design
- Modern/RETRO look
- Headers for the following verticals:
About Me
Books
Articles
TV
Hire Me
Speaking
Consulting
Classes
School Visits
Press
Blaaaahhhhg! (Blog)
Contact Me

```html
<!DOCTYPE html>
<html lang="en">
<head>
<meta charset="utf-8">
<title>Delia Brunwick — Professional Writer. Amateur Mom.</title>
<link rel="stylesheet" href="https://fonts.googleapis.com/css2?family=Open+Sans:wght@300;400;600;700&display=swap">
<style>
:root{
  --white:#ffffff;
  --ink:#1d1d1d;
  --muted:#555a5e;
  --grey-line:#c9c4c8;
  --mauve:#a89aa5;
  --teal-mid:#6aa6ae;
  --teal-foot:#6fcbb5;
  --teal-foot-low:#8ad3d8;
  --cyan:#27d3df;
  --pink:#e8207a;
  --btn:#5c5a50;
  --panel-blue:#b8dfe8;
}
*{margin:0;padding:0;box-sizing:border-box}
html,body{width:760px;height:1200px;overflow:hidden}
body{position:relative;font-family:"Open Sans",Arial,sans-serif;color:var(--ink);background:var(--white)}
.abs{position:absolute}

/* header */
.site-header{left:0;top:0;width:760px;height:106px;background:var(--white)}
.brand-name{left:186px;top:34px;font-size:22px;font-weight:700;color:var(--ink);white-space:nowrap}
.brand-divider{left:378px;top:20px;width:1px;height:62px;background:#d8d8d8}
.brand-tagline{left:400px;top:43px;font-size:12.5px;color:var(--muted);white-space:nowrap}

/* main area */
.main-area{left:0;top:106px;width:760px;height:714px;background:linear-gradient(180deg,var(--mauve) 0%,#9c9aa8 45%,var(--teal-mid) 100%)}

.main-nav{left:194px;top:106px;width:372px;height:39px;background:var(--white)}
.main-nav .stripe{position:absolute;left:0;top:0;width:100%;height:3px;display:flex}
.main-nav .stripe span{flex:1}
.main-nav ul{list-style:none;display:flex;flex-wrap:nowrap;justify-content:space-between;width:100%;height:100%;align-items:center;padding-right:2px}
.main-nav li{font-size:6.1px;letter-spacing:-.1px;white-space:nowrap;color:#3c3c3c;padding:0 1px;height:100%;display:flex;align-items:center;position:relative}
.main-nav li.active{background:var(--cyan);color:var(--white);padding:0 4px}
.main-nav li.has-sub::after{content:"";position:absolute;left:50%;bottom:9px;margin-left:-2px;border:2px solid transparent;border-top-color:#3c3c3c}

.books-panel{left:194px;top:145px;width:372px;height:191px;background:var(--white);box-shadow:0 10px 10px -6px rgba(0,0,0,.35)}
.panel-title{left:14px;top:12px;font-size:14.5px;font-weight:400;color:#333}
.social-list{right:10px;top:10px;display:flex;gap:3px;font-size:4.8px;color:#8a8a8a;white-space:nowrap}
.book-cover{width:51px;height:68px}
.book-one{left:14px;top:45px;background:linear-gradient(180deg,#6ee02a,#d8197a 55%,#6ee02a)}
.book-two{left:199px;top:45px;width:49px;background:linear-gradient(180deg,#f4ee9a,#e9d9a6)}
.book-text{font-size:5.6px;line-height:1.45;color:#444;width:95px}
.book-text .title{color:var(--pink)}
.book-text p{margin-bottom:5px}
.book-divider{left:187px;top:40px;width:1px;height:128px;background:#e3e3e3}
.btn-more{display:inline-block;background:var(--btn);color:var(--white);font-size:7px;padding:2px 9px;border-radius:2px}
.dots{left:326px;top:172px;display:flex;gap:2px}
.dots span{width:6px;height:6px;border-radius:50%;border:1px solid #999;background:var(--white)}
.dots span.on{background:#555}

.section-title{font-size:14px;font-weight:300;color:#3a3a3a}
.rule{height:1px;background:var(--grey-line)}
.news-text{font-size:6.8px;line-height:1.5;color:#222;width:240px}
.news-text .title{color:var(--pink)}
.media{display:block}

.tweets-box{left:460px;top:408px;width:106px;height:337px;background:var(--white);overflow:hidden}
.tweet{position:absolute;left:4px;width:92px;font-size:4.8px;line-height:1.45;color:#444}
.tweet .avatar{position:absolute;left:0;top:0;width:17px;height:17px;background:#7a5a52}
.tweet .who{margin-left:23px;font-size:5.6px;color:#222;font-weight:600}
.tweet .handle{margin-left:23px;font-size:5.4px;color:#777;margin-bottom:5px}
.tweets-scroll{left:98px;top:2px;width:6px;height:333px;background:#eee}
.tweets-scroll span{position:absolute;left:1px;top:2px;width:4px;height:140px;background:#bbb;border-radius:2px}
.follow-btn{left:494px;top:388px;width:72px;height:12px;background:var(--white);border:1px solid #bbb;border-radius:2px;font-size:5.6px;line-height:10px;padding-left:4px;color:#333;white-space:nowrap;overflow:hidden}

/* footer band */
.footer-band{left:0;top:820px;width:760px;height:323px;background:linear-gradient(180deg,var(--teal-foot),var(--teal-foot-low));border-top:3px solid #e6f6f2}
.band-title{font-size:14px;font-weight:400;color:var(--white)}
.band-rule{height:3px;background:var(--white)}
.photo-grid{left:196px;top:882px;width:134px;height:256px;background:var(--panel-blue);display:grid;grid-template-columns:50px 50px;gap:13px 14px;padding:10px 10px}
.photo-grid div{width:50px;height:50px}
.blog-item{position:absolute;left:366px;width:191px;font-size:6px;line-height:1.5;color:#1e3b40}
.blog-item .title{color:var(--pink);font-size:7px}
.blog-item .date{font-size:7px;color:#23343a;margin:6px 0 8px}
.blog-item .excerpt{width:155px}
.blog-item .btn-more{position:absolute;right:0;bottom:-2px}
.blog-item .rule-dark{position:absolute;left:0;right:0;bottom:-10px;height:1px;background:#4c8b93}

/* site footer */
.site-footer{left:0;top:1143px;width:760px;height:57px;background:var(--white)}
.footer-mail{left:205px;top:21px;font-size:6px;color:#444}
.footer-mail b{font-size:10px;margin-right:6px}
.footer-mail a{color:#1b7f91;text-decoration:none}
.footer-links{left:493px;top:25px;font-size:6px;color:#444}
.to-top{left:630px;top:32px;width:16px;height:16px;background:#b8d9c4}
</style>
</head>
<body>

<header class="site-header abs">
  <div class="brand-name abs">Delia Brunwick</div>
  <div class="brand-divider abs"></div>
  <div class="brand-tagline abs">Professional Writer. Amateur Mom.</div>
</header>

<main class="main-area abs"></main>

<nav class="main-nav abs">
  <div class="stripe">
    <span style="background:#27d3df"></span><span style="background:#f5c400"></span><span style="background:#7bd12a"></span><span style="background:#e8207a"></span><span style="background:#8e44c8"></span><span style="background:#27a8e0"></span><span style="background:#f39a1e"></span><span style="background:#7bd12a"></span><span style="background:#e23b3b"></span><span style="background:#27d3df"></span><span style="background:#f5c400"></span><span style="background:#8e44c8"></span><span style="background:#e8207a"></span>
  </div>
  <ul>
    <li class="active">main</li>
    <li class="has-sub">about me</li>
    <li>books</li>
    <li>articles</li>
    <li>tv</li>
    <li>hire me</li>
    <li>speaking</li>
    <li>consulting</li>
    <li>classes</li>
    <li>school visits</li>
    <li>press</li>
    <li>blog</li>
    <li>contact me</li>
  </ul>
</nav>

<section class="books-panel abs">
  <h2 class="panel-title abs">Some Of My Books</h2>
  <div class="social-list abs"><span>Drovely</span><span>Quenlo</span><span>Brimsetta</span><span>vostraloom</span><span>Tarvio +</span></div>

  <div class="book-cover book-one abs" role="img" aria-label="Book cover for Got Glam?, a pink cup on a green background"></div>
  <div class="book-text abs" style="left:78px;top:45px">
    <p><span class="title">Got Glam?</span> The Busy Parent's Guide to Looking Sharp, Laughing Often and Driving a Station Wagon.<br>Lindenfield, 2011.</p>
    <p>Got Glam? cheers on the modern parent. It's time to stand tall, embrace your inner mom and be counted!</p>
  </div>
  <span class="btn-more abs" style="left:135px;top:134px">more</span>

  <div class="book-divider abs"></div>

  <div class="book-cover book-two abs" role="img" aria-label="Book cover for The Maid of Honor's Field Manual, pale yellow with drawn figures"></div>
  <div class="book-text abs" style="left:260px;top:45px">
    <p><span class="title">The Maid of Honor's Field Manual</span></p>
    <p>Lindenfield, 1997, reissued 2002</p>
    <p>A funny handbook for wedding attendants, full of tips and how-to for the walk down the aisle...and after.</p>
  </div>
  <span class="btn-more abs" style="left:320px;top:134px">more</span>

  <div class="dots abs"><span></span><span></span><span class="on"></span></div>
</section>

<section class="latest-news">
  <h2 class="section-title abs" style="left:194px;top:356px">Latest News !</h2>
  <div class="rule abs" style="left:194px;top:380px;width:242px"></div>
  <div class="news-text abs" style="left:196px;top:386px">
    My children's book, "Splash Goes the Evening" is now AVAILABLE in fine book stores (yes...and crappy ones too) everywhere! Read a few of the GREAT reviews <span class="title">HERE!!</span><br>
    And check out the book trailer by my oh-so-talented illustrator and friend, Tomas Verrill (creator of "Pip and the Mighty Moose" on Kidvista)!!!!
  </div>
  <div class="media abs" role="img" aria-label="Video player showing the animated book trailer for Splash Goes the Evening" style="left:196px;top:444px;width:213px;height:121px;background:linear-gradient(180deg,#2a2a2a 0 9%,#c9b27a 9%,#5aa7c4 55%,#3f6f4a 91%,#1f1f1f 91%)"></div>
  <span class="btn-more abs" style="left:197px;top:575px">more</span>
  <div class="rule abs" style="left:194px;top:602px;width:242px"></div>

  <div class="news-text abs" style="left:196px;top:618px;line-height:2.2">
    <span class="title">Got Glam?</span> The Busy Parent's Guide to Looking Sharp, Laughing Often and Driving a Station Wagon: out now!
  </div>
  <div class="media abs" role="img" aria-label="Book cover for Got Glam?" style="left:196px;top:668px;width:50px;height:67px;background:linear-gradient(180deg,#6ee02a,#d8197a 55%,#6ee02a)"></div>
  <div class="media abs" role="img" aria-label="Video player showing a book reading" style="left:266px;top:655px;width:149px;height:95px;background:linear-gradient(180deg,#2a2a2a 0 10%,#6b3a3a 10%,#8a6e5e 55%,#3a4c3a 88%,#1f1f1f 88%)"></div>
  <span class="btn-more abs" style="left:197px;top:772px">more</span>
  <div class="rule abs" style="left:194px;top:797px;width:242px"></div>
</section>

<aside class="tweets">
  <h2 class="section-title abs" style="left:460px;top:356px">Tweets</h2>
  <div class="follow-btn abs">Follow @DeliaBrunwick</div>
  <div class="tweets-box abs">
    <div class="tweet" style="top:6px"><div class="avatar"></div><div class="who">Delia Brunwick</div><div class="handle">@DeliaBrunwick</div>JUST A REMINDER that THIS SATURDAY I'll be reading at the Corner Book Nook in West Park. Come say hi!</div>
    <div class="tweet" style="top:74px"><div class="avatar"></div><div class="who">Delia Brunwick</div><div class="handle">@DeliaBrunwick</div>Check out my latest piece: 10 reasons the school run is a contact sport. Link in bio today.</div>
    <div class="tweet" style="top:142px"><div class="avatar"></div><div class="who">Delia Brunwick</div><div class="handle">@DeliaBrunwick</div>JUST A REMINDER that THIS SATURDAY I'll be reading at the Corner Book Nook in West Park. Come say hi!</div>
    <div class="tweet" style="top:210px"><div class="avatar"></div><div class="who">Delia Brunwick</div><div class="handle">@DeliaBrunwick</div>Check out my latest piece: 10 reasons the school run is a contact sport. Link in bio today.</div>
    <div class="tweet" style="top:278px"><div class="avatar"></div><div class="who">Delia Brunwick</div><div class="handle">@DeliaBrunwick</div>JUST A REMINDER that THIS SATURDAY I'll be reading at the Corner Book Nook today.</div>
    <div class="tweets-scroll abs"><span></span></div>
  </div>
  <span class="btn-more abs" style="left:518px;top:752px">more</span>
</aside>

<section class="footer-band abs"></section>

<section class="photo-feed">
  <h2 class="band-title abs" style="left:198px;top:848px">Brimsetta</h2>
  <div class="band-rule abs" style="left:196px;top:870px;width:134px"></div>
  <div class="photo-grid abs" role="img" aria-label="Grid of eight photo thumbnails in blue and orange light tones">
    <div style="background:linear-gradient(135deg,#1a3a8a,#e0802a)"></div>
    <div style="background:linear-gradient(135deg,#9ec0e8,#2a5aa8)"></div>
    <div style="background:linear-gradient(135deg,#0e2a5a,#6aa8e0)"></div>
    <div style="background:linear-gradient(135deg,#1a1a4a,#e85aa8)"></div>
    <div style="background:linear-gradient(135deg,#1a3a8a,#e0802a)"></div>
    <div style="background:linear-gradient(135deg,#9ec0e8,#2a5aa8)"></div>
    <div style="background:linear-gradient(135deg,#0e2a5a,#6aa8e0)"></div>
    <div style="background:linear-gradient(135deg,#1a1a4a,#e85aa8)"></div>
  </div>
</section>

<section class="blog-feed">
  <h2 class="band-title abs" style="left:366px;top:848px">Blog</h2>
  <div class="band-rule abs" style="left:366px;top:870px;width:191px"></div>

  <article class="blog-item" style="top:886px">
    <div class="title">FamilyNook.com Clip of Me! From Carpool Lane to Comedy Club</div>
    <div class="date">Sunday, August 4, 2013</div>
    <div class="excerpt">I just came across this clip while I was searching for my own name (in my defense, I am prepping for the book launch). Okay, I admit it, I like to look myself up. Happy?!</div>
    <span class="btn-more">more</span><div class="rule-dark"></div>
  </article>

  <article class="blog-item" style="top:982px">
    <div class="title">Summer Camp Photo Albums – Blessing or Curse?</div>
    <div class="date">Thursday, July 18, 2013</div>
    <div class="excerpt">Are you a slave to refreshing those camp pictures like I am?! Five kids, two hours, NEVER a smile. Please tell me I'm not alone...</div>
    <span class="btn-more">more</span><div class="rule-dark"></div>
  </article>

  <article class="blog-item" style="top:1062px">
    <div class="title">A Fix For Marriage? ...I Doubt It...</div>
    <div class="date">Thursday, October 6, 2011</div>
    <div class="excerpt">Just letting you know you can check out my latest article on the Daily Lantern in reply to a "relationship guru" who says he has a fix.</div>
    <span class="btn-more">more</span>
  </article>

  <svg class="abs" style="left:372px;top:1135px" width="14" height="8" viewBox="0 0 14 8"><path d="M0 8 L7 0 L14 8 Z" fill="#ffffff"/></svg>
</section>

<footer class="site-footer abs">
  <div class="footer-mail abs"><b>@</b>E-Mail : <a href="mailto:hello@deliabrunwick.com">hello@deliabrunwick.com</a></div>
  <div class="footer-links abs">2013 &nbsp;PRIVACY POLICY</div>
  <div class="to-top abs">
    <svg width="16" height="16" viewBox="0 0 16 16"><path d="M8 4 L8 12 M5 7 L8 4 L11 7" stroke="#ffffff" stroke-width="1.4" fill="none"/></svg>
  </div>
</footer>

</body>
</html>
```